Looking to create a business card with images representing lawn care (i.e. grass, lawn mower, etc.) Maybe put a crown over the letter Q. The details for the card is listed below:

Len Dabrowski Jr.
President
Cedar Glen, MD

Tall Fern Landscaping
Services: lawn mowing, trimming, blowing, edging, spring and fall clean-up, pruning, weeding, mulching, and more

call today for a free estimate: 240-417-2853

```html
<!DOCTYPE html>
<html lang="en">
<head>
<meta charset="utf-8">
<title>Tall Fern Landscaping – Business Card</title>
<link href="https://fonts.googleapis.com/css2?family=Roboto:wght@400;500;700;900&display=swap" rel="stylesheet">
<style>
  :root {
    --page: #e9ebe7;
    --grass-light: #8fd14a;
    --grass-mid: #5ea92a;
    --grass-deep: #2f7a18;
    --brand-green: #5bb030;
    --ink: #1e1e1e;
    --ink-soft: #333333;
    --paper: #ffffff;
  }
  * { box-sizing: border-box; margin: 0; padding: 0; }
  html, body { width: 1200px; height: 900px; overflow: hidden; }
  body {
    background: var(--page);
    font-family: "Roboto", Arial, sans-serif;
    color: var(--ink);
    position: relative;
  }
  .card {
    position: absolute;
    width: 700px;
    height: 400px;
    border-radius: 4px;
    overflow: hidden;
    box-shadow: 0 6px 18px rgba(0,0,0,0.18);
  }
  .card--front { left: 250px; top: 30px; }
  .card--back  { left: 250px; top: 470px; background: var(--paper); }

  .lawn-photo {
    position: absolute;
    inset: 0;
    background:
      linear-gradient(160deg, rgba(255,255,255,0.08) 0%, rgba(0,0,0,0) 45%, rgba(0,0,0,0.18) 100%),
      linear-gradient(180deg, var(--grass-light) 0%, var(--grass-mid) 55%, var(--grass-deep) 100%);
  }

  /* Front */
  .front-brand {
    position: absolute;
    inset: 0;
    display: flex;
    flex-direction: column;
    align-items: center;
    justify-content: center;
    gap: 8px;
  }
  .front-brand__name,
  .front-brand__sub {
    font-weight: 900;
    text-transform: uppercase;
    color: var(--ink);
    line-height: 1;
  }
  .front-brand__name { font-size: 66px; letter-spacing: 1px; }
  .front-brand__sub  { font-size: 40px; letter-spacing: 4px; }

  /* Back */
  .back-lawn {
    position: absolute;
    left: 0; top: 0; bottom: 0;
    width: 300px;
  }
  .back-lawn .lawn-photo {
    background:
      linear-gradient(180deg, rgba(255,255,255,0.1) 0%, rgba(0,0,0,0) 40%, rgba(0,0,0,0.15) 100%),
      linear-gradient(180deg, #a6dc6a 0%, var(--grass-mid) 50%, #3f8a1e 100%);
  }
  .estimate {
    position: absolute;
    left: 34px;
    top: 212px;
    color: var(--paper);
    font-weight: 700;
    font-size: 21px;
    line-height: 1.3;
  }
  .estimate__phone {
    margin-top: 14px;
    font-size: 24px;
    letter-spacing: 0.5px;
  }

  .details {
    position: absolute;
    left: 330px;
    right: 24px;
    top: 34px;
  }
  .details__brand {
    font-weight: 900;
    font-size: 30px;
    text-transform: uppercase;
    color: var(--ink);
    line-height: 1.05;
  }
  .person { margin-top: 24px; }
  .person__name {
    font-weight: 700;
    font-size: 22px;
    color: var(--brand-green);
  }
  .person__role, .person__place {
    font-size: 16px;
    color: var(--ink-soft);
    line-height: 1.35;
  }
  .services { margin-top: 16px; }
  .services__title {
    font-weight: 500;
    font-size: 17px;
    color: var(--brand-green);
    text-transform: uppercase;
    margin-bottom: 4px;
  }
  .services__row {
    display: flex;
    flex-wrap: nowrap;
    gap: 14px;
    font-size: 15px;
    color: var(--ink-soft);
    line-height: 1.65;
  }
  .service { display: inline-flex; align-items: center; gap: 4px; white-space: nowrap; }
  .tick { width: 13px; height: 13px; flex: none; }
  .contact {
    margin-top: 12px;
    font-size: 16px;
    color: var(--ink-soft);
  }
  .contact__label { color: var(--brand-green); font-weight: 500; }
</style>
</head>
<body>

<section class="card card--front" aria-label="Business card front">
  <div class="lawn-photo" role="img" aria-label="Striped freshly mowed green lawn"></div>
  <div class="front-brand">
    <span class="front-brand__name">Tall Fern</span>
    <span class="front-brand__sub">Landscaping</span>
  </div>
</section>

<section class="card card--back" aria-label="Business card back">
  <div class="back-lawn">
    <div class="lawn-photo" role="img" aria-label="Close-up of green grass"></div>
    <div class="estimate">
      <p>Call today for a<br>free estimate</p>
      <p class="estimate__phone">240-417-2853</p>
    </div>
  </div>

  <div class="details">
    <div class="details__brand">Tall Fern<br>Landscaping</div>

    <div class="person">
      <p class="person__name">Len Dabrowski Jr.</p>
      <p class="person__role">President</p>
      <p class="person__place">Cedar Glen, MD</p>
    </div>

    <div class="services">
      <p class="services__title">Our Services</p>
      <div class="services__row">
        <span class="service"><svg class="tick" viewBox="0 0 14 14"><path d="M2 7.5l3 3 7-8" fill="none" stroke="#5bb030" stroke-width="2.4" stroke-linecap="round" stroke-linejoin="round"/></svg>Edging</span>
        <span class="service"><svg class="tick" viewBox="0 0 14 14"><path d="M2 7.5l3 3 7-8" fill="none" stroke="#5bb030" stroke-width="2.4" stroke-linecap="round" stroke-linejoin="round"/></svg>Weeding</span>
        <span class="service"><svg class="tick" viewBox="0 0 14 14"><path d="M2 7.5l3 3 7-8" fill="none" stroke="#5bb030" stroke-width="2.4" stroke-linecap="round" stroke-linejoin="round"/></svg>Pruning</span>
        <span class="service"><svg class="tick" viewBox="0 0 14 14"><path d="M2 7.5l3 3 7-8" fill="none" stroke="#5bb030" stroke-width="2.4" stroke-linecap="round" stroke-linejoin="round"/></svg>Lawn mowing</span>
      </div>
      <div class="services__row">
        <span class="service"><svg class="tick" viewBox="0 0 14 14"><path d="M2 7.5l3 3 7-8" fill="none" stroke="#5bb030" stroke-width="2.4" stroke-linecap="round" stroke-linejoin="round"/></svg>Blowing</span>
        <span class="service"><svg class="tick" viewBox="0 0 14 14"><path d="M2 7.5l3 3 7-8" fill="none" stroke="#5bb030" stroke-width="2.4" stroke-linecap="round" stroke-linejoin="round"/></svg>Mulching</span>
        <span class="service"><svg class="tick" viewBox="0 0 14 14"><path d="M2 7.5l3 3 7-8" fill="none" stroke="#5bb030" stroke-width="2.4" stroke-linecap="round" stroke-linejoin="round"/></svg>Trimming</span>
      </div>
      <div class="services__row">
        <span class="service"><svg class="tick" viewBox="0 0 14 14"><path d="M2 7.5l3 3 7-8" fill="none" stroke="#5bb030" stroke-width="2.4" stroke-linecap="round" stroke-linejoin="round"/></svg>Spring and fall clean-up</span>
        <span class="service"><svg class="tick" viewBox="0 0 14 14"><path d="M2 7.5l3 3 7-8" fill="none" stroke="#5bb030" stroke-width="2.4" stroke-linecap="round" stroke-linejoin="round"/></svg>And more</span>
      </div>
    </div>

    <p class="contact"><span class="contact__label">Mail :</span> len.dabrowski@tallfernmail.com</p>
  </div>
</section>

</body>
</html>
```